Graduation Day Sale Banner Ad for Website

We need a banner for our upscale jewelry website. Banner must have a classy high end look. The size of the banner must be 1187 × 400. I have attached pieces we would like used (some or all). The banner is for a Graduation Day sale that we are running. The banner should say "Graduation Day Gifts on Sale"

Target Market(s)

Wealthy individuals looking to buy graduation gifts for their children

Industry/Entity Type

Jewelry

Requirements
Must have
• Must match the look and feel of the website (www.velmira-studio.com)

```html
<!DOCTYPE html>
<html lang="en">
<head>
<meta charset="utf-8">
<title>Graduation Day Gifts on Sale</title>
<link rel="stylesheet" href="https://fonts.googleapis.com/css2?family=Oswald:wght@600&family=Cormorant+Garamond:wght@500&display=swap">
<style>
  :root {
    --band: #d9b79c;
    --bg-light: #f6ebe2;
    --bg-mid: #efdccd;
    --headline: #8b7161;
    --sale: #5b2d12;
    --gold-light: #ecd3a6;
    --gold-mid: #d8b377;
    --silver-light: #eceef2;
    --silver-mid: #c9ccd6;
  }
  html, body {
    margin: 0;
    padding: 0;
    width: 1200px;
    height: 404px;
    overflow: hidden;
    background: #ffffff;
  }
  .banner {
    position: relative;
    width: 1200px;
    height: 404px;
    overflow: hidden;
    background:
      radial-gradient(ellipse 60% 70% at 45% 55%, var(--bg-light) 0%, rgba(246,235,226,0) 70%),
      linear-gradient(90deg, var(--bg-mid) 0%, var(--bg-light) 45%, var(--bg-mid) 100%);
  }
  .banner::before,
  .banner::after {
    content: "";
    position: absolute;
    left: 0;
    width: 100%;
    height: 7px;
    background: var(--band);
  }
  .banner::before { top: 0; }
  .banner::after { bottom: 0; }

  .rings-photo {
    position: absolute;
    left: 44px;
    top: 124px;
    width: 406px;
    height: 214px;
    border-radius: 18px;
    background: linear-gradient(180deg, var(--gold-mid) 0%, var(--gold-light) 62%, rgba(236,211,166,0.35) 100%);
  }

  .pendant-photo {
    position: absolute;
    left: 956px;
    top: 7px;
    width: 210px;
    height: 258px;
    border-radius: 0 0 18px 18px;
    background: linear-gradient(180deg, var(--silver-light) 0%, var(--silver-mid) 100%);
  }

  .headline {
    position: absolute;
    margin: 0;
    font-family: "Oswald", "Arial Narrow", sans-serif;
    font-weight: 600;
    color: var(--headline);
    text-transform: uppercase;
    line-height: 1;
    white-space: nowrap;
  }
  .headline--top {
    left: 405px;
    top: 55px;
    font-size: 66px;
    letter-spacing: 5px;
  }
  .headline--middle {
    left: 583px;
    top: 134px;
    font-size: 72px;
    letter-spacing: 9px;
  }
  .sale-word {
    position: absolute;
    left: 775px;
    top: 226px;
    margin: 0;
    font-family: "Cormorant Garamond", "Times New Roman", serif;
    font-weight: 500;
    font-size: 142px;
    line-height: 1;
    color: var(--sale);
    letter-spacing: -1px;
    white-space: nowrap;
  }
</style>
</head>
<body>
  <main class="banner">
    <div class="rings-photo" role="img" aria-label="Photo of gold and two-tone rings, one set with pearls and diamonds"></div>
    <div class="pendant-photo" role="img" aria-label="Photo of a diamond heart pendant with two sapphires on a chain"></div>
    <h1 class="headline headline--top">Graduation Day</h1>
    <p class="headline headline--middle">Gifts On</p>
    <p class="sale-word">SALE</p>
  </main>
</body>
</html>
```